Propose a revamped landing page

One template we like eg is https://www.tornavo.com but but cluttered Our logo and colors are attached to our logo and colors are printed on a white background what we have. So font usage ...
Number of Pages Required
1 page

```html
<!DOCTYPE html>
<html lang="en">
<head>
<meta charset="utf-8">
<title>Wattwise – Never pay too much for electricity &amp; gas again</title>
<link href="https://fonts.googleapis.com/css2?family=Poppins:wght@300;400;500;600;700&display=swap" rel="stylesheet">
<style>
  :root {
    --orange: #f9ab1f;
    --orange-deep: #f7a21a;
    --ink: #3a4047;
    --dark: #2f353c;
    --text: #555b61;
    --white: #ffffff;
    --light: #f2f2f2;
    --teal: #1fa99b;
    --sky: #cdeef3;
    --line: #e6e6e6;
  }
  * { box-sizing: border-box; margin: 0; padding: 0; }
  html, body { width: 1200px; height: 2748px; overflow: hidden; }
  body { font-family: "Poppins", sans-serif; color: var(--ink); background: var(--white); position: relative; }

  /* hero */
  .hero { position: absolute; left: 0; top: 0; width: 1200px; height: 647px; background: linear-gradient(180deg, var(--orange) 0%, var(--orange-deep) 100%); }
  .brand { position: absolute; left: 86px; top: 28px; display: flex; align-items: center; gap: 8px; font-weight: 700; font-size: 36px; line-height: 44px; color: var(--white); letter-spacing: -0.5px; white-space: nowrap; }
  .brand-dot { width: 18px; height: 18px; border-radius: 50%; background: var(--ink); flex: none; }
  .nav { position: absolute; left: 310px; top: 41px; display: flex; gap: 21px; font-size: 13.5px; line-height: 20px; color: var(--white); white-space: nowrap; }
  .btn { position: absolute; display: flex; align-items: center; justify-content: center; border-radius: 40px; font-size: 15px; font-weight: 400; white-space: nowrap; }
  .btn-dark { background: var(--dark); color: var(--white); }
  .btn-outline { border: 1.5px solid var(--white); color: var(--white); }
  .btn-orange { background: var(--orange); color: var(--white); }
  .hero-title { position: absolute; left: 86px; top: 236px; font-size: 45px; line-height: 54px; font-weight: 700; color: var(--white); }
  .hero-lead { position: absolute; left: 86px; top: 358px; width: 540px; font-size: 16px; line-height: 26px; font-weight: 300; color: var(--white); }
  .hero-art { position: absolute; left: 749px; top: 171px; width: 366px; height: 366px; border-radius: 50%; background: linear-gradient(180deg, var(--sky) 0%, var(--sky) 45%, var(--teal) 60%, #0d7f74 100%); }

  /* headings */
  .section-title { position: absolute; left: 0; width: 1200px; text-align: center; font-size: 32px; font-weight: 700; }
  .rule { position: absolute; left: 574px; width: 52px; height: 2px; background: var(--orange); }

  /* cards */
  .card { position: absolute; top: 823px; width: 324px; height: 291px; background: var(--white); border-radius: 22px; box-shadow: 0 6px 22px rgba(0,0,0,0.12); text-align: center; }
  .card svg { position: absolute; left: 130px; top: 34px; }
  .card-title { position: absolute; left: 0; width: 100%; top: 126px; font-size: 22px; font-weight: 600; color: var(--ink); }
  .card-rule { position: absolute; left: 136px; top: 175px; width: 52px; height: 2px; background: var(--orange); }
  .card-text { position: absolute; left: 40px; width: 244px; top: 200px; font-size: 14px; line-height: 24px; color: var(--text); }

  /* dark band */
  .powers { position: absolute; left: 0; top: 1194px; width: 1200px; height: 658px; background: var(--dark); }
  .powers-art { position: absolute; left: 399px; top: 1365px; width: 400px; height: 247px; border-radius: 120px 120px 90px 90px; background: linear-gradient(180deg, #2fb3a6 0%, #26a597 50%, #474c52 100%); }
  .powers-text { position: absolute; left: 310px; width: 580px; top: 1657px; text-align: center; font-size: 14px; line-height: 26px; color: var(--white); }

  /* steps */
  .hero-figure { position: absolute; left: 440px; top: 2006px; width: 311px; height: 348px; border-radius: 50%; background: radial-gradient(circle, #fff36b 0%, #ffd21d 50%, rgba(255,210,29,0) 72%); }
  .step-num { position: absolute; width: 62px; height: 62px; border-radius: 50%; border: 1.5px solid var(--line); background: var(--white); color: var(--orange); font-size: 21px; font-weight: 500; display: flex; align-items: center; justify-content: center; }
  .step-title { position: absolute; font-size: 22px; font-weight: 600; color: var(--ink); white-space: nowrap; }
  .step-text { position: absolute; font-size: 14px; line-height: 24px; color: var(--text); }

  /* footer */
  .footer { position: absolute; left: 0; top: 2631px; width: 1200px; height: 117px; background: var(--light); }
  .footer-brand { position: absolute; left: 86px; top: 38px; display: flex; align-items: center; gap: 8px; font-size: 28px; font-weight: 700; color: var(--orange); }
  .footer-brand .brand-dot { width: 14px; height: 14px; }
  .footer-nav { position: absolute; left: 288px; top: 50px; font-size: 12px; color: var(--text); white-space: nowrap; }
  .footer-copy { position: absolute; left: 819px; top: 50px; font-size: 12px; color: var(--text); white-space: nowrap; }
  .social { position: absolute; left: 1099px; top: 50px; width: 16px; height: 16px; border-radius: 50%; background: var(--dark); }
</style>
</head>
<body>

<header class="hero">
  <div class="brand">Wattwise <span class="brand-dot"></span></div>
  <nav class="nav">
    <span>That's How It Works</span><span>Prices</span><span>Ask?</span><span>About Us</span><span>Operations</span><span>Experience</span><span>Press</span>
  </nav>
  <a class="btn btn-dark" style="left:938px;top:31px;width:176px;height:39px;">Register Now</a>
  <h1 class="hero-title">Never pay too much for<br>electricity &amp; gas again</h1>
  <p class="hero-lead">Gone are the days of bad deals, tedious rate comparison and boring exchange forms.</p>
  <a class="btn btn-dark" style="left:86px;top:456px;width:176px;height:39px;">Register Now</a>
  <a class="btn btn-outline" style="left:280px;top:456px;width:174px;height:39px;">Read More</a>
  <div class="hero-art" role="img" aria-label="Illustration of a signpost in a green landscape with a setting sun"></div>
</header>

<h2 class="section-title" style="top:716px;">Register once, always save</h2>
<div class="rule" style="top:783px;"></div>

<article class="card" style="left:86px;">
  <svg width="64" height="56" viewBox="0 0 64 56" fill="none" stroke="#9aa0a6" stroke-width="1.5" stroke-linejoin="round">
    <path d="M4 24 L60 4 L44 50 L30 32 Z"/><path d="M30 32 L60 4"/><path d="M30 32 L28 46 L36 40"/>
  </svg>
  <div class="card-title">Independently</div>
  <div class="card-rule"></div>
  <p class="card-text">We work only for you. In order to remain independent.</p>
</article>

<article class="card" style="left:438px;">
  <svg width="64" height="60" viewBox="0 0 64 60" fill="none" stroke="#9aa0a6" stroke-width="1.5">
    <circle cx="24" cy="22" r="12"/><circle cx="24" cy="22" r="5"/>
    <path d="M24 4v6M24 34v6M6 22h6M36 22h6M11 9l4 4M33 31l4 4M11 35l4-4M33 13l4-4"/>
    <circle cx="46" cy="44" r="8"/><circle cx="46" cy="44" r="3"/>
    <path d="M46 32v4M46 52v4M34 44h4M54 44h4"/>
  </svg>
  <div class="card-title">Automatically</div>
  <div class="card-rule"></div>
  <p class="card-text">You sign up once and we'll do the rest. All automatically.</p>
</article>

<article class="card" style="left:790px;">
  <svg width="68" height="58" viewBox="0 0 68 58" fill="none" stroke="#9aa0a6" stroke-width="1.5" stroke-linejoin="round">
    <path d="M14 16 L20 4 L50 10 L48 16"/><path d="M22 16 L28 8 L44 12"/>
    <rect x="4" y="16" width="58" height="38" rx="4"/>
    <path d="M62 28 H48 a6 6 0 0 0 0 12 H62"/><circle cx="50" cy="34" r="2"/>
  </svg>
  <div class="card-title">Fair</div>
  <div class="card-rule"></div>
  <p class="card-text">Wattwise members save more in total. Despite service charge.</p>
</article>

<section class="powers"></section>
<h2 class="section-title" style="top:1253px;color:var(--white);">The cheapest of all super powers</h2>
<div class="rule" style="top:1318px;"></div>
<div class="powers-art" role="img" aria-label="Illustration of a town at dusk inside a cloud shape with a savings badge of up to 850 euros"></div>
<p class="powers-text">It is a long established fact that a reader will be distracted by the readable content of a page when looking at its layout.</p>
<a class="btn btn-orange" style="left:513px;top:1737px;width:174px;height:37px;">Register Now</a>

<h2 class="section-title" style="top:1921px;">How do I become Wattwise?</h2>
<div class="rule" style="top:1989px;"></div>
<div class="hero-figure" role="img" aria-label="Illustration of a flying superhero in a green suit and red cape on a yellow burst"></div>

<div class="step-num" style="left:350px;top:2138px;">1</div>
<div class="step-title" style="left:100px;width:232px;text-align:right;top:2146px;">Once login</div>
<p class="step-text" style="left:60px;width:272px;text-align:right;top:2188px;">Upload financial statements. Select preferences. Finish the registration.</p>

<div class="step-num" style="left:784px;top:2138px;">2</div>
<div class="step-title" style="left:868px;top:2146px;">Automatic</div>
<p class="step-text" style="left:868px;width:250px;top:2188px;">Fare change We pick the cheapest fare for you and carry out the change automatically.</p>

<div class="step-num" style="left:409px;top:2385px;">3</div>
<div class="step-title" style="left:493px;top:2391px;">Sit back and save money</div>
<p class="step-text" style="left:493px;top:2434px;">Always switch automatically to the low fare.</p>

<a class="btn btn-orange" style="left:513px;top:2497px;width:174px;height:37px;">Register Now</a>

<footer class="footer">
  <div class="footer-brand">Wattwise <span class="brand-dot"></span></div>
  <div class="footer-nav">That's How It Works &nbsp;|&nbsp; Prices &nbsp;|&nbsp; Ask? &nbsp;|&nbsp; About Us &nbsp;|&nbsp; Operations &nbsp;|&nbsp; Experience &nbsp;|&nbsp; Press</div>
  <div class="footer-copy">© Copyright 2019. All Rights Reserved.</div>
  <div class="social" aria-label="Social profile"></div>
</footer>

</body>
</html>
```